Chiropractic office needs updated web site

take the information/content from my existing website and redesign it to be more efficient and modern looking. i have a logo already designed that i have provided the files for. my office sees primarily athletes and their families and is geared toward active, healthy people who have sports injuries.
Updates

i originally started the project in february 2019 but am now just able to post the project. i need a new deadline calculated from todays (6-9-19) date.

Target Market(s)

injured athletes looking for a specific type of chiropractor.

Industry/Entity Type

Health Care

Contact Information for Business Card

I have a logo already designed and will provide that to all designers!

Coding

Coded - Design and coding required

Number of Pages Required

1 page

Font styles to use
Sans Serif

Colors

Designer to choose colors to be used in the design.

Requirements
Must have
• the current information/content already contained in my current website, belvanspinefit.com. i want this info redesigned and/or transferred to a new template. i will also provide new updated photos for use on the new site!
Nice to have
• modern, minimalist, creative looking website
Should not have
• typical medical website with boring, over-used stock photos of doctors, nurses and generic family types

```html
<!DOCTYPE html>
<html lang="en">
<head>
<meta charset="utf-8">
<title>Belvan Chiropractic + Sports Therapy</title>
<link href="https://fonts.googleapis.com/css2?family=Poppins:wght@400;500;600&family=Nunito+Sans:wght@600&display=swap" rel="stylesheet">
<style>
:root{
  --ink:#1f2f3e;
  --bar:#24323f;
  --accent:#e2245a;
  --accent-soft:#fdeef2;
  --muted:#7d8797;
  --hero-bg:#f3f3f4;
  --band:#eef3f4;
  --white:#ffffff;
  --rule:#e6e8eb;
  --mat:#6cc6e4;
}
*{margin:0;padding:0;box-sizing:border-box}
html,body{width:1200px;height:1200px;overflow:hidden;background:var(--white)}
body{position:relative;font-family:'Poppins',sans-serif;color:var(--ink)}
.abs{position:absolute}

.notice-bar{left:0;top:0;width:1200px;height:32px;background:var(--bar);color:var(--white);font-size:9px;font-weight:500;display:flex;align-items:center;justify-content:center;gap:6px}
.notice-bar a{color:var(--white);text-decoration:underline}
.notice-bar .close{margin-left:14px;font-size:11px}

.contact-icon{width:38px;height:38px;border-radius:50%;background:var(--accent-soft);display:flex;align-items:center;justify-content:center}
.contact-label{font-size:9px;color:var(--muted)}
.contact-value{font-size:14.5px;font-weight:500;color:var(--ink);margin-top:4px}

.brand{left:510px;top:44px;display:flex;align-items:center;gap:8px}
.brand-dot{width:32px;height:32px;border-radius:50%;background:var(--accent)}
.brand-name{font-size:19px;font-weight:500;color:#1ab0e0;letter-spacing:1px}

.header-rule{left:263px;top:93px;width:686px;height:1px;background:var(--rule)}
.main-nav{left:298px;top:100px;display:flex;font-family:'Nunito Sans',sans-serif;font-size:9.6px;font-weight:600}
.main-nav a{color:var(--ink);text-decoration:none;padding:0 14px;height:31px;line-height:24px}
.main-nav a.active{color:var(--accent);border-bottom:2px solid var(--accent)}
.search{left:938px;top:106px}

.hero{left:0;top:131px;width:1200px;height:420px;background:var(--hero-bg)}
.hero-photo{left:437px;top:160px;width:748px;height:358px;background:linear-gradient(180deg,#ffffff 0%,#eceef1 30%,#d3d7dd 60%,#a9dcee 85%,var(--mat) 100%)}
.hero-title{left:64px;top:222px;font-size:30.5px;font-weight:600;line-height:63px;color:var(--ink)}
.hero-sub{left:72px;top:367px;font-size:14.5px;font-weight:500;color:var(--muted)}
.play{left:71px;top:407px;width:32px;height:32px;border-radius:50%;background:var(--accent);display:flex;align-items:center;justify-content:center}
.play-label{left:116px;top:415px;font-size:9px;font-weight:500;color:var(--ink);border-bottom:1px solid var(--rule);padding-bottom:2px}
.hero-base{left:0;top:549px;width:231px;height:3px;background:#d8d9db}

.finder{left:231px;top:520px;width:742px;height:64px;background:var(--white);box-shadow:0 12px 30px rgba(30,40,60,.08);display:flex}
.finder-field{width:313px;padding:14px 22px;border-right:1px solid var(--rule);position:relative}
.finder-field:nth-child(2){width:300px;border-right:none}
.finder-label{font-size:8.5px;color:var(--muted)}
.finder-value{font-size:12.5px;font-weight:500;margin-top:8px}
.caret{position:absolute;right:22px;top:37px;width:0;height:0;border-left:3.5px solid transparent;border-right:3.5px solid transparent;border-top:4px solid var(--muted)}
.finder-btn{flex:1;background:var(--accent);color:var(--white);font-size:11.5px;font-weight:600;display:flex;align-items:center;justify-content:center}

.tile{box-shadow:0 10px 24px rgba(30,40,60,.14)}
.tile-a{left:63px;top:689px;width:172px;height:113px;background:linear-gradient(135deg,#2c3a2f,#4f7b52 60%,#c9b468)}
.tile-b{left:404px;top:654px;width:170px;height:113px;background:linear-gradient(120deg,#b9764a,#e0b98f 55%,#d8d3cc)}
.tile-c{left:195px;top:745px;width:290px;height:203px;background:linear-gradient(160deg,#33405a,#4d5872 45%,#8a5a5a 80%,#b3433e)}
.tile-d{left:93px;top:911px;width:157px;height:105px;background:linear-gradient(150deg,#6b4a34,#2f3a35 60%,#9aa6a8)}
.orbit{left:396px;top:862px}
.heart-badge{left:440px;top:906px;width:70px;height:70px;border-radius:50%;background:var(--white);box-shadow:0 8px 24px rgba(30,40,60,.12);display:flex;align-items:center;justify-content:center}

.eyebrow{font-size:8.5px;font-weight:600;letter-spacing:2.6px;color:var(--muted)}
.about-eyebrow{left:675px;top:702px}
.about-title{left:675px;top:727px;font-size:23px;font-weight:600;line-height:32.5px;width:320px}
.about-text{left:675px;top:848px;width:300px;font-size:10.3px;line-height:17.8px;color:var(--muted)}
.about-link{left:675px;top:947px;font-size:9px;font-weight:500;color:var(--accent);border-bottom:1px solid var(--accent);padding-bottom:1px}

.services-band{left:0;top:1067px;width:1200px;height:133px;background:var(--band)}
.services-eyebrow{left:0;top:1140px;width:1200px;text-align:center}
.services-title{left:0;top:1164px;width:1200px;text-align:center;font-size:25px;font-weight:600}
</style>
</head>
<body>

<div class="abs notice-bar">
  <svg width="9" height="8" viewBox="0 0 10 9"><path d="M5 9L1 5A2.4 2.4 0 0 1 5 1.6 2.4 2.4 0 0 1 9 5z" fill="#e2245a"/></svg>
  <span>Are you a Carer, Occupational Therapist or Physiotherapist? <a>Join our Mendwell.</a></span>
  <span class="close">×</span>
</div>

<div class="abs contact-icon" style="left:48px;top:62px">
  <svg width="18" height="18" viewBox="0 0 24 24" fill="none" stroke="#e2245a" stroke-width="1.6"><path d="M6 3l3 4-2 2c1 2.5 3 4.5 5.5 5.5l2-2 4 3-2 3C10 18 5 13 4 5z"/><path d="M15 4a5 5 0 0 1 4 4M15 7a2 2 0 0 1 2 2"/></svg>
</div>
<div class="abs" style="left:98px;top:64px">
  <div class="contact-label">Call us for any question</div>
  <div class="contact-value">(+00)555.210.44</div>
</div>

<div class="abs brand">
  <div class="brand-dot"></div>
  <div class="brand-name">BELVAN CHIROPRACTIC</div>
</div>

<div class="abs" style="left:1000px;top:64px">
  <div class="contact-label">Call us for any question</div>
  <div class="contact-value">Download Now</div>
</div>
<div class="abs contact-icon" style="left:1119px;top:62px">
  <svg width="18" height="18" viewBox="0 0 24 24" fill="none" stroke="#e2245a" stroke-width="1.6"><circle cx="11" cy="3.5" r="1.6"/><path d="M11 6v7h6l2 6M8 10a6 6 0 1 0 8 8"/></svg>
</div>

<div class="abs header-rule"></div>
<nav class="abs main-nav">
  <a class="active">Home</a><a>Treatments Offered</a><a>New Patient Paperwork</a><a>Stretching</a><a>Photo Gallery</a><a>Social</a><a>Location</a>
</nav>
<svg class="abs search" width="11" height="11" viewBox="0 0 12 12" fill="none" stroke="#1f2f3e" stroke-width="1.7"><circle cx="5" cy="5" r="3.8"/><path d="M8 8l3 3"/></svg>

<section class="abs hero"></section>
<div class="abs hero-photo" role="img" aria-label="Therapist guiding an athlete through a balance stretch on a blue mat"></div>
<h1 class="abs hero-title">Belvan Chiropractic +<br>Sports Therapy</h1>
<p class="abs hero-sub">Because your health matters the most</p>
<div class="abs play"><svg width="10" height="11" viewBox="0 0 10 11"><path d="M1 0l9 5.5L1 11z" fill="#fff"/></svg></div>
<div class="abs play-label">How We Work</div>
<div class="abs hero-base"></div>

<form class="abs finder">
  <div class="finder-field"><div class="finder-label">Select your location</div><div class="finder-value">Choose a location</div><span class="caret"></span></div>
  <div class="finder-field"><div class="finder-label">Select your service</div><div class="finder-value">Choose a service</div><span class="caret"></span></div>
  <div class="finder-btn">Get care now</div>
</form>

<div class="abs tile tile-a" role="img" aria-label="Volleyball player setting the ball during an indoor match"></div>
<div class="abs tile tile-b" role="img" aria-label="Signed portrait of an athlete thanking the clinic"></div>
<div class="abs tile tile-c" role="img" aria-label="Volleyball match in a packed arena"></div>
<div class="abs tile tile-d" role="img" aria-label="Two team players in green jerseys"></div>
<svg class="abs orbit" width="158" height="158" viewBox="0 0 158 158" fill="none" stroke="#c4c8cf" stroke-width="1.2" stroke-dasharray="1 4"><circle cx="79" cy="79" r="77"/><circle cx="79" cy="79" r="58"/></svg>
<div class="abs heart-badge">
  <svg width="32" height="26" viewBox="0 0 32 26" fill="none" stroke="#e2245a" stroke-width="3.4" stroke-linejoin="round"><path d="M16 23L4 11a6 6 0 0 1 12-4 6 6 0 0 1 12 4L16 23z"/><path d="M10 12l6 6 6-6"/></svg>
</div>

<div class="abs eyebrow about-eyebrow">ABOUT US</div>
<h2 class="abs about-title">We established cooperation with various global partners.</h2>
<p class="abs about-text">We've combined a new kind of doctor's experience that blends the highest level of health care with exceptional service. People can enroll membership by paying only an annual membership fee of just $129.</p>
<a class="abs about-link">More About Us</a>

<section class="abs services-band"></section>
<div class="abs eyebrow services-eyebrow">OUR SERVICES</div>
<h2 class="abs services-title">Treatments offered</h2>

</body>
</html>
```